Corwell Holdings Business Cards

Hello. I need business cards designed with our new logo. I'd like to see at least 3 different designs. At least one with a dark background, and at least one with a white background. Maybe one with gray or blue for the background. Play with gradient colors and maybe even insert a pic of a skyline in the background of one or more of them. Use your judgement. We will need 2 cards printed. They need to accommodate the employee name, title, company address, phone, email, and website. Thanks.

Target Market(s)

Wealthy mature investors.

Contact Information for Business Card

Single-sided, professional, clean design that incorporates our logo.

Font styles to use
Sans Serif

Requirements
Must have
• Our new logo needs to be featured on it. (See attached.)
• Employee Name (In all CAPS)
• Title
• Street Address, City, ST Zip Code
• Cell Phone #, Email Address, Website Address
Nice to have
• Design that blends well with our new logo and its colors, or a city scape or other graphic design that looks like an apartment complex in the background. Blues and grays are nice, but use your judgement.
Should not have
• Modern or oriental looking designs or bright colors.

```html
<!DOCTYPE html>
<html lang="en">
<head>
<meta charset="utf-8">
<title>Corwell Holdings Business Cards</title>
<link rel="stylesheet" href="https://fonts.googleapis.com/css2?family=Montserrat:wght@500;600&family=Open+Sans:wght@400;600&display=swap">
<style>
  :root {
    --brand-blue: #29a6df;
    --band-grey: #4b4b4d;
    --text-grey: #5d5d60;
    --paper: #ffffff;
    --paper-shade: #f2f3f4;
    --backdrop: #dfe1e4;
    --rule-grey: #8d8f92;
  }
  * { box-sizing: border-box; margin: 0; padding: 0; }
  html, body { width: 1200px; height: 800px; overflow: hidden; }
  body {
    background: var(--backdrop);
    display: flex;
    flex-direction: column;
    align-items: center;
    justify-content: center;
    gap: 36px;
    font-family: "Open Sans", Arial, sans-serif;
  }
  .card {
    position: relative;
    width: 630px;
    height: 360px;
    overflow: hidden;
    box-shadow: 0 6px 18px rgba(0,0,0,0.18);
  }

  /* Front */
  .card--front {
    background: var(--brand-blue);
    display: flex;
    flex-direction: column;
    align-items: center;
    justify-content: center;
    gap: 34px;
    color: var(--paper);
  }
  .wordmark {
    display: flex;
    align-items: center;
    gap: 14px;
    font-family: "Montserrat", Arial, sans-serif;
    font-weight: 600;
    text-transform: uppercase;
    letter-spacing: 1px;
    line-height: 1;
  }
  .wordmark__square { width: 34px; height: 34px; background: currentColor; }
  .wordmark__name { font-size: 34px; }
  .card--front .website {
    font-family: "Montserrat", Arial, sans-serif;
    font-weight: 500;
    font-size: 14px;
    letter-spacing: 4px;
    text-transform: uppercase;
  }

  /* Back */
  .card--back { background: var(--paper); }
  .skyline {
    position: absolute;
    inset: 0 0 108px 0;
    background: linear-gradient(180deg, var(--paper) 0%, var(--paper-shade) 45%, #d9dbdd 78%, #e9eaeb 100%);
  }
  .card--back .wordmark {
    position: absolute;
    top: 62px;
    right: 44px;
    color: var(--brand-blue);
  }
  .card--back .wordmark__name { font-size: 27px; }
  .card--back .wordmark__square { width: 28px; height: 28px; }
  .divider {
    position: absolute;
    top: 122px;
    right: 44px;
    width: 300px;
    height: 1px;
    background: var(--rule-grey);
  }
  .person {
    position: absolute;
    left: 40px;
    bottom: 124px;
    display: flex;
    align-items: baseline;
    gap: 8px;
  }
  .person__name {
    font-family: "Montserrat", Arial, sans-serif;
    font-weight: 600;
    font-size: 22px;
    color: var(--brand-blue);
    text-transform: uppercase;
  }
  .person__title { font-size: 15px; color: var(--text-grey); }
  .person__line {
    position: absolute;
    left: 40px;
    bottom: 114px;
    width: 250px;
    height: 1px;
    background: var(--rule-grey);
  }
  .contact-band {
    position: absolute;
    left: 0; right: 0; bottom: 14px;
    height: 94px;
    background: var(--band-grey);
    color: #f1f1f1;
    display: flex;
    align-items: center;
    padding: 0 40px;
    font-size: 13.5px;
  }
  .accent-stripe {
    position: absolute;
    left: 0; right: 0; bottom: 0;
    height: 14px;
    background: var(--brand-blue);
  }
  .contact-list { list-style: none; display: flex; flex-direction: column; gap: 6px; }
  .contact-list li { display: flex; align-items: center; gap: 10px; }
  .contact-list svg { width: 14px; height: 14px; flex: none; }
  .band-rule { width: 1px; height: 34px; background: #c9c9c9; margin: 0 auto; }
  .address { display: flex; align-items: flex-start; gap: 10px; line-height: 1.4; }
  .address svg { width: 12px; height: 16px; margin-top: 2px; flex: none; }
</style>
</head>
<body>

<section class="card card--front" aria-label="Card front">
  <div class="wordmark">
    <span class="wordmark__square"></span>
    <span class="wordmark__name">Corwell Holdings, LLC</span>
  </div>
  <p class="website">www.corwellholdings.com</p>
</section>

<section class="card card--back" aria-label="Card back">
  <div class="skyline" role="img" aria-label="Faded black and white city skyline reflected in a river"></div>

  <div class="wordmark">
    <span class="wordmark__square"></span>
    <span class="wordmark__name">Corwell Holdings, LLC</span>
  </div>
  <div class="divider"></div>

  <div class="person">
    <span class="person__name">Daniel Reeve</span>
    <span class="person__title">| Founder</span>
  </div>
  <div class="person__line"></div>

  <div class="contact-band">
    <ul class="contact-list">
      <li>
        <svg viewBox="0 0 14 14" aria-hidden="true"><rect x="3" y="1" width="8" height="12" rx="1.5" fill="none" stroke="var(--brand-blue)" stroke-width="1.6"/></svg>
        480.555.0192
      </li>
      <li>
        <svg viewBox="0 0 14 14" aria-hidden="true"><rect x="1" y="3" width="12" height="8" fill="var(--brand-blue)"/><path d="M1 3 L7 8 L13 3" fill="none" stroke="var(--band-grey)" stroke-width="1.2"/></svg>
        info@corwellholdings.com
      </li>
    </ul>
    <span class="band-rule"></span>
    <div class="address">
      <svg viewBox="0 0 12 16" aria-hidden="true"><path d="M6 1 C3 1 1 3.2 1 5.8 C1 9.5 6 15 6 15 C6 15 11 9.5 11 5.8 C11 3.2 9 1 6 1 Z" fill="var(--brand-blue)"/><circle cx="6" cy="5.8" r="1.8" fill="var(--band-grey)"/></svg>
      <p>PO BOX 418, Mesa Avenue<br>3rd Lane, Arizona 85201</p>
    </div>
  </div>
  <div class="accent-stripe"></div>
</section>

</body>
</html>
```